Packaging design for a modern organic cosmetic product

We are an organic cosmetic brand using Aloe Vera. We are looking for new packaging design for cardboard tubes similar to the following:
https://img7.pelmorastatic.net/kf/Q4ba183c72d904617ae2093541cf62b08K.jpg
This package will be used to insert 2 or 3 products as a combo.
The printing will be done in two colors. We just need a base design for the tube and the cap. Later a sticker may be stick on the tube to specify the content of the combo. So the design should be workable with or without an additional sticker. At this time we are only looking for the base tube design with some artwork without the sticker design. The artwork can be based on our logo, color and theme. Our logo is attached herewith. Our company is located in the Algarve, South Portugal. Our products are regional and related to Sea, Sunshine, Sand and Aloe Vera. The products are based on natural ingredients, vegan and organic.
Please let me know if you have any questions. I am also attaching the vector file of the logo.

```html
<!DOCTYPE html>
<html lang="en">
<head>
<meta charset="utf-8">
<title>Solmaré – Tube Packaging</title>
<link href="https://fonts.googleapis.com/css2?family=Montserrat:wght@400;500&display=swap" rel="stylesheet">
<style>
  :root {
    --backdrop: #efe6d7;
    --aloe-green: #8a9465;
    --charcoal: #333336;
    --paper: #ffffff;
    --cream: #f3f1e6;
    --pattern-light: #f6f6f4;
    --badge-grey: #9a9a9a;
    --badge-green: #2e9a3c;
  }
  html, body {
    margin: 0;
    padding: 0;
    width: 1200px;
    height: 977px;
    overflow: hidden;
    background: var(--backdrop);
  }
  .artboard { display: block; width: 1200px; height: 977px; }
  .brand-type {
    font-family: "Montserrat", sans-serif;
    font-weight: 500;
  }
  .tagline {
    font-family: "Montserrat", sans-serif;
    font-weight: 400;
    letter-spacing: 2.4px;
  }
</style>
</head>
<body>
<svg class="artboard" viewBox="0 0 1200 977" xmlns="http://www.w3.org/2000/svg">
  <defs>
    <path id="cap-arc" d="M 785 300 A 92 92 0 0 1 935 200"/>
  </defs>

  <!-- Cap label -->
  <g class="cap-label">
    <circle cx="872" cy="267" r="111" fill="var(--charcoal)" role="img" aria-label="Dark lid face with faint aloe leaf pattern"/>
    <circle cx="872" cy="267" r="104" fill="none" stroke="var(--aloe-green)" stroke-width="1"/>
    <text class="tagline" font-size="12.5" fill="var(--cream)">
      <textPath href="#cap-arc">NATURAL INGREDIENTS</textPath>
    </text>
    <circle cx="872" cy="267" r="48" fill="var(--cream)"/>
    <text class="brand-type" x="872" y="272" font-size="14" fill="var(--aloe-green)" text-anchor="middle" letter-spacing="1">Solmaré</text>
  </g>

  <!-- Tube wrap label -->
  <g class="wrap-label">
    <rect x="718" y="529" width="318" height="242" fill="var(--pattern-light)" role="img" aria-label="White band with faint aloe leaf outline pattern"/>
    <rect x="718" y="482" width="318" height="47" fill="var(--aloe-green)"/>
    <path d="M 817 529 H 935 V 698 A 59 59 0 0 1 817 698 Z" fill="var(--aloe-green)"/>
    <rect x="718" y="771" width="318" height="122" fill="var(--charcoal)"/>

    <circle cx="876" cy="698" r="50" fill="var(--paper)"/>
    <text class="brand-type" x="876" y="703" font-size="14" fill="var(--aloe-green)" text-anchor="middle" letter-spacing="1">Solmaré</text>

    <path d="M 876 740 C 880 752 891 762 891 775 A 15 15 0 0 1 861 775 C 861 762 872 752 876 740 Z" fill="var(--aloe-green)"/>

    <text class="tagline" x="878" y="815" font-size="14" fill="var(--paper)" text-anchor="middle" letter-spacing="1">NATURAL</text>
    <text class="tagline" x="878" y="833" font-size="14" fill="var(--paper)" text-anchor="middle">INGREDIENTS</text>

    <circle cx="751" cy="861" r="14" fill="var(--paper)" stroke="var(--badge-grey)" stroke-width="2"/>
    <circle cx="800" cy="861" r="15" fill="none" stroke="var(--badge-green)" stroke-width="2.5"/>
    <circle cx="800" cy="861" r="9" fill="var(--badge-green)"/>

    <line x1="843" y1="861" x2="1036" y2="861" stroke="var(--cream)" stroke-width="1"/>
  </g>
</svg>
</body>
</html>
```